Nu Upsilon civil engineering orgnization activities flyer

we need flyer design for Nu Upsilon civil engineering honor society in University of Brenmoor for science and technology. the flyer contain the schedule of the expected activity. the design should have a purple color and Nu Upsilon Key and logo (you will find them in the attached file) and the design should have something referring to civil engineering

Industry/Entity Type

Education

Colors
6b449b

Requirements
Must have
• Nu Upsilon logo, key, motto
Nice to have
• civil engineering samples, purple color

```html
<!DOCTYPE html>
<html lang="en">
<head>
<meta charset="utf-8">
<title>Nu Upsilon Activities Flyer</title>
<link rel="stylesheet" href="https://fonts.googleapis.com/css2?family=Montserrat:wght@400;600;700&family=Open+Sans:wght@400&display=swap">
<style>
:root{
  --purple:#6b449b;
  --purple-deep:#5a3690;
  --yellow:#f5c81e;
  --ink:#1b1b1b;
  --paper:#ececec;
  --line:#222;
  --bg:#e6e2dc;
}
*{margin:0;padding:0;box-sizing:border-box}
html,body{width:1200px;height:1200px;overflow:hidden;background:var(--bg)}
.flyer{position:absolute;left:197px;top:30px;width:806px;height:1140px;
  background:radial-gradient(ellipse at 50% 40%,#fafafa 0%,#e4e4e4 100%);
  box-shadow:0 4px 18px rgba(0,0,0,.25);overflow:hidden;font-family:"Montserrat",sans-serif;color:var(--ink)}
.hero{position:absolute;left:0;top:0;width:806px;height:364px;
  background:linear-gradient(180deg,#cfcfcf 0%,#b5b5b5 45%,#5a5a5a 80%,#2e2e2e 100%)}
.brand{position:absolute;left:38px;top:36px;display:flex;align-items:center;gap:10px;
  font-weight:700;font-size:40px;color:var(--purple);letter-spacing:.5px}
.brand-dot{width:14px;height:14px;border-radius:50%;background:var(--purple)}
.inset{position:absolute;left:593px;top:34px;width:172px;height:206px;background:#fff;padding:6px;box-shadow:0 2px 6px rgba(0,0,0,.35)}
.inset-fill{width:100%;height:100%;background:linear-gradient(160deg,#c7cbe0 0%,#e7dcb4 50%,#c9a53a 100%)}
.bar-purple{position:absolute;left:792px;top:283px;width:14px;height:351px;background:var(--purple)}
.bar-yellow{position:absolute;left:0;top:523px;width:14px;height:350px;background:var(--yellow)}
.section-title{position:absolute;left:0;width:806px;top:372px;text-align:center;font-weight:700;font-size:19px;color:var(--purple);letter-spacing:.5px}
.schedule{position:absolute;left:42px;top:405px;width:723px;border-collapse:collapse;font-family:"Open Sans",sans-serif;font-size:14.5px;text-align:center}
.schedule th,.schedule td{border:1.5px solid var(--line);font-weight:400;line-height:1.35}
.schedule th{vertical-align:top;padding-top:5px;height:51px}
.schedule td{height:32px}
.schedule tr.tall td{height:51px}
.block{position:absolute;font-size:11.5px;line-height:1.15}
.block h2{font-size:19px;font-weight:700;color:var(--purple);line-height:1}
.block h3{font-size:12px;font-weight:700;margin-top:0}
.block p{margin-bottom:13px}
.service{left:72px;top:764px;width:310px}
.vdivider{position:absolute;left:403px;top:733px;width:1px;height:300px;background:#cfcfcf}
.hdivider{position:absolute;left:455px;top:876px;width:304px;height:1px;background:#d3d3d3}
.icon{position:absolute;width:52px;height:52px}
.icon-social{left:418px;top:776px}
.icon-init{left:418px;top:918px}
.social{left:484px;top:764px;width:310px}
.initiation{left:484px;top:909px;width:318px}
.footer{position:absolute;left:0;top:1044px;width:806px;height:96px;background:var(--purple-deep);
  display:flex;align-items:center;justify-content:center;gap:12px}
.footer-dot{width:14px;height:14px;border-radius:50%;background:var(--yellow);margin-bottom:14px}
.footer-lockup{display:flex;flex-direction:column;align-items:flex-end;line-height:1}
.footer-name{font-size:36px;font-weight:700;color:#fff}
.footer-tag{font-size:9px;color:#fff;margin-top:5px}
</style>
</head>
<body>
<div class="flyer">
  <div class="hero" role="img" aria-label="Black and white photo of construction cranes over a building under construction"></div>
  <div class="brand"><span class="brand-dot"></span>Nu Upsilon</div>
  <div class="inset"><div class="inset-fill" role="img" aria-label="Collage of the society key with conception, design and construction images"></div></div>
  <div class="bar-purple"></div>
  <div class="bar-yellow"></div>

  <div class="section-title">MEETING</div>
  <table class="schedule">
    <colgroup><col style="width:103px"><col style="width:116px"><col style="width:91px"><col style="width:108px"><col style="width:167px"><col style="width:138px"></colgroup>
    <tr><th>Meeting<br>No.</th><th>Date</th><th>Time</th><th>Location</th><th>Name</th><th>Company</th></tr>
    <tr><td>1</td><td>9/8/2015</td><td>7 PM</td><td>ENG 124</td><td>Dr. Halvorsen</td><td></td></tr>
    <tr><td>2</td><td>9/22/2015</td><td>7 PM</td><td>ENG 124</td><td>Milo Brandt</td><td>Metro Waterworks</td></tr>
    <tr class="tall"><td>3</td><td>10/6/2015</td><td>7 PM</td><td>ENG 124</td><td>Owen Kessler</td><td>Ft. Ashgrove<br>Base</td></tr>
    <tr><td>4</td><td>10/20/2015</td><td>7 PM</td><td>ENG 124</td><td>Jordan Ellery</td><td>Korvo Inc.</td></tr>
    <tr><td>5</td><td>11/3/2015</td><td>7 PM</td><td>ENG 124</td><td>Scavenger Hunt</td><td>Social</td></tr>
    <tr class="tall"><td>6</td><td>11/17/2015</td><td>7 PM</td><td>ENG124</td><td>Nomination/<br>Dale Whitcomb</td><td>Harlan Finch</td></tr>
    <tr><td>7</td><td>12/1/2015</td><td>7 PM</td><td>ENG 124</td><td>Elections</td><td>-</td></tr>
  </table>

  <div class="block service">
    <h2>SERVICE</h2>
    <h3>Pine Hollow Nature Area Service Day</h3>
    <p>Saturday, Oct 24, 11 am<br>Pine Hollow Nature Area, Brenmoor, MO 65999,<br>United States</p>
    <h3>Neighbors Alliance Service Day</h3>
    <p>Saturday, Nov 7, 11 am<br>The Neighbors Alliance Resale Shop, 2200<br>N Archer Ave, Brenmoor, MO 65999, United States</p>
    <h3>Tri Valley Animal Shelter Volunteer Day</h3>
    <p>Thursday, Nov 12, 12 pm<br>Tri Valley Animal Shelter, 745 E Maplewood St,<br>Eastfield, MO 65990, United States</p>
  </div>

  <div class="vdivider"></div>

  <svg class="icon icon-social" viewBox="0 0 52 52" fill="none" stroke="#6b449b" stroke-width="2.2">
    <circle cx="12" cy="9" r="5"/><circle cx="40" cy="9" r="5"/><circle cx="26" cy="15" r="5"/>
    <path d="M3 34V22a4 4 0 0 1 4-4h10"/><path d="M49 34V22a4 4 0 0 0-4-4H35"/>
    <path d="M17 48V29a4 4 0 0 1 4-4h10a4 4 0 0 1 4 4v19"/>
  </svg>
  <div class="block social">
    <h2>SOCIAL</h2>
    Nu Upsilon Smoker<br>
    Bowling /Lanternlight Lanes (1038 Crown Road)<br>
    Wednesday, October 28th/ 9:00 PM<br>
    Plaque Signing/ When: December 8th/ the Hub
  </div>

  <div class="hdivider"></div>

  <svg class="icon icon-init" viewBox="0 0 52 52" fill="#6b449b">
    <path d="M22 2h8v7l5 2 5-5 6 6-5 5 2 5h7v8h-7l-2 5 5 5-6 6-5-5-5 2v7h-8v-7l-5-2-5 5-6-6 5-5-2-5H2v-8h7l2-5-5-5 6-6 5 5 5-2z"/>
    <circle cx="26" cy="26" r="11" fill="#f2f2f2"/>
  </svg>
  <div class="block initiation">
    <h2>INITIATION</h2>
    12/12/2015 5 PM-6PM &nbsp; ENG 314<br>
    6:30PM initiation diner<br>
    Marlowe's- 1100 North Lincoln Street, Eastfield,
  </div>

  <div class="footer">
    <span class="footer-dot"></span>
    <div class="footer-lockup">
      <span class="footer-name">Nu Upsilon</span>
      <span class="footer-tag">The Civil Engineering Honor Society</span>
    </div>
  </div>
</div>
</body>
</html>
```